Flyer/Broschürre für Ambulanter Betreuungsdienst
Zielgruppe
Ambulanter Betreuungsdienst,Dienstleistungen für Senioren und Menschen mit Beeinträchtigung
Nach Paragraph 43b 45a/b & 53b SGBXI
Unterstützung im Alltag:
-Begleitung zu Arztbesuchen,Therapien &Terminbegleitung aller Art,
-Hilfe beim Einkaufen & Besorgungen + Transport
-Unterstützung bei der Tagesstrukturierung & Organisation im Alltag
-Erinnerungsservice zb. Einahme von Medikamenten ggbf. Kontrolle
-Begleitung zu Sportveranstaltungen,Theater uvm.
für zuverlässige Sicherheit und Orientierung.
-Gemeinsames Spazieren gehen ( Bewegungsangebote)
- Lesen & Vorlesen
-Gemeinsames Kochen und geselschaft leisten beim essen.
-Unterstützung bei Terminplanungen,Hilfe bei der komunikation mit Medizinischen Personal.
Soziale Betreuung & Aktivierung:
-Geselschaft leisten,Gespräche führen ;
-Freizeitaktivitäten Planen & Durchführen
-Gemeinsames Lesen und Vorlesen
-Karten & Brettspiele spielen
-Malen & Basteln
-Briefe schreiben,Emails verfassen
-Gemeinsam alte interessen wecken und neue finden.
-Angehörige entlasten
-kommunikation & Informationsaustausch über Fortschritte und Bedürfnisse
-Betreuung & Aktivierung für Menschen mit Demenz
-Erinnerungspflege,Biografie Arbeit
-Individuelle Betreuung
-Kurz und Langzeit Betreuung
-Nachtpflege
-Bewegungsangebote
-Spiele spielen zb. Brett & Gemeinschsftsspiele
Dienstleistungen Haushaltsbereich
-Reinigung von Böden(Saugen & Wischen)
-Reinigung Küche und Bad
-Bett frisch Beziehen
-Fenster Reinigung (innen & außen)
-Haustiere versorgen (mit dem Hund spazieren gehen)
-Wäsche waschen
-Dekorieren
-uvm
Aufgabenstellung
Freundliches Design , vertrauenswürdiges Erscheinungsbild mit warmen Farben.
Firmenname ( Kornblatt) logo sollte einen Kornblatt darstellen.
Slogan Text:
Verlässlichkeit und Fürsorge mit Herz & Verstand.
Format soll handlich und nicht zu klein sein,damit Senioren es gut lesen bzw erkennen können.

```html
<!DOCTYPE html>
<html lang="de">
<head>
<meta charset="utf-8">
<title>Kornblatt – Ambulanter Betreuungsdienst Flyer</title>
<link href="https://fonts.googleapis.com/css2?family=Montserrat:ital,wght@0,400;0,500;0,600;0,700;1,400&family=Kalam:wght@700&display=swap" rel="stylesheet">
<style>
:root{
  --blue:#2c5c96;
  --blue-dark:#23497a;
  --orange:#c6763a;
  --orange-soft:#d99a68;
  --brown:#5a3a22;
  --ink:#2a2a2a;
  --cream:#f7f1e8;
  --meadow-1:#efe3cf;
  --meadow-2:#d9bb93;
  --meadow-3:#b99a78;
  --stage:#e9ecef;
}
*{box-sizing:border-box;margin:0;padding:0}
html,body{width:1200px;height:4106px;overflow:hidden}
body{background:var(--stage);font-family:"Montserrat",Arial,sans-serif;color:var(--ink);
  display:flex;flex-direction:column;align-items:center;justify-content:center;gap:90px}
.spread{width:1120px;height:792px;display:flex;box-shadow:0 10px 30px rgba(0,0,0,.18)}
.panel{position:relative;width:560px;height:792px;overflow:hidden;background:#fff}
.panel + .panel{border-left:1px solid rgba(0,0,0,.06)}
.photo{position:absolute;left:0;right:0}
.meadow{background:linear-gradient(180deg,rgba(255,255,255,0) 0%,var(--meadow-1) 25%,var(--meadow-2) 70%,var(--meadow-3) 100%)}
.band{position:absolute;left:0;right:0;bottom:0;height:70px;background:var(--blue);color:#fff;
  font-weight:600;font-size:27px;display:flex;align-items:center;padding-left:36px;z-index:2}
.center{text-align:center}

/* back panel */
.back-title{position:absolute;top:50px;left:0;right:0;color:var(--blue);font-size:29px;font-weight:600;line-height:1.25}
.back-sub{position:absolute;top:150px;left:60px;right:60px;color:var(--orange);font-size:19px;line-height:1.3}
.contact-tab{position:absolute;top:260px;left:60px;right:60px;height:80px;background:var(--blue);color:#fff;
  border-radius:10px 10px 0 0;font-size:21px;font-weight:500;line-height:1.25;display:flex;align-items:center;justify-content:center;text-align:center}
.contact-list{position:absolute;top:360px;left:80px;right:40px;list-style:none}
.contact-list li{display:flex;align-items:center;gap:16px;font-size:17px;font-weight:600;color:var(--ink);margin-bottom:20px}
.contact-list li.phone{font-size:23px}
.contact-list li .val{font-weight:500;color:var(--blue)}
.contact-list li.phone .val{color:var(--ink)}
.contact-list svg{flex:none;width:26px;height:26px;fill:var(--blue-dark)}
.badge{position:absolute;right:60px;bottom:100px;width:150px;height:120px;border:3px solid var(--blue-dark);border-radius:50%;opacity:.8}

/* front panel */
.brand{position:absolute;top:60px;left:0;right:0;text-align:center}
.brand-mark{width:90px;height:90px;border-radius:50%;background:var(--blue);margin:0 auto 10px}
.brand-name{color:var(--blue);font-weight:700;font-size:52px;line-height:1}
.brand-line{color:var(--blue);font-weight:600;font-size:26px;margin-top:6px}
.brand-target{color:var(--orange);font-size:17px;margin-top:4px}
.slogan{position:absolute;top:325px;left:0;right:0;text-align:center;font-family:"Kalam",cursive;color:var(--brown);font-size:31px;line-height:1.2}

/* inside */
.head{position:absolute;top:0;left:0;right:0;height:140px;background:var(--blue);color:#fff;
  clip-path:polygon(0 0,100% 0,100% 82%,0 100%);font-size:28px;font-weight:500;line-height:1.3;
  display:flex;align-items:flex-start;justify-content:center;padding-top:34px;text-align:center}
.head.caps{height:90px;clip-path:none;font-size:27px;padding-top:26px;text-transform:uppercase;letter-spacing:.5px}
.intro{position:absolute;top:155px;left:50px;right:30px;font-size:19px;line-height:1.35;color:#7b6a5b;text-align:center}
.intro b{color:var(--orange);font-weight:600}
.features{position:absolute;top:320px;left:100px;width:380px;background:rgba(255,255,255,.85);padding:12px 18px;list-style:none}
.features li{display:flex;align-items:center;gap:10px;font-size:14.5px;margin:6px 0}
.features li b{font-weight:600}
.ico{flex:none;width:22px;height:22px;border-radius:4px;background:var(--orange)}
.ico.blue{background:var(--blue)}
.sec-title{position:absolute;color:var(--blue);font-weight:600;font-size:24px}
.svc{position:absolute;font-size:12.5px;line-height:1.3;padding-left:16px}
.svc b{font-weight:700}
.svc.house{font-size:13px;line-height:1.25}
.illus{position:absolute;background:var(--orange-soft);border-radius:40%;opacity:.85}
</style>
</head>
<body>

<section class="spread outside">
  <div class="panel back-panel">
    <div class="photo meadow" style="top:230px;bottom:0" role="img" aria-label="Foto einer sonnigen Blumenwiese im Abendlicht"></div>
    <h2 class="back-title center">Wir beraten Sie gerne<br>persönlich &amp; unverbindlich</h2>
    <p class="back-sub center">Gemeinsam finden wir die passende Unterstützung für Ihre individuelle Situation.</p>
    <div class="contact-tab">Kornblatt – Ambulanter<br>Betreuungsdienst</div>
    <ul class="contact-list">
      <li class="phone"><svg viewBox="0 0 24 24"><path d="M6.6 10.8c1.4 2.8 3.8 5.1 6.6 6.6l2.2-2.2c.3-.3.7-.4 1-.2 1.1.4 2.3.6 3.6.6.6 0 1 .4 1 1V20c0 .6-.4 1-1 1C10.6 21 3 13.4 3 4c0-.6.4-1 1-1h3.5c.6 0 1 .4 1 1 0 1.3.2 2.5.6 3.6.1.3 0 .7-.2 1z"/></svg><span>Telefon: <span class="val">0XXX / XXXXXXX</span></span></li>
      <li><svg viewBox="0 0 24 24"><path d="M2 5h20v14H2zM3 6l9 7 9-7v1.5l-9 7-9-7z"/></svg><span>E-Mail: <span class="val">info@kornblatt-betreuung.de</span></span></li>
      <li><svg viewBox="0 0 24 24"><path d="M12 2a10 10 0 100 20 10 10 0 000-20zm0 2c.9 0 2.2 1.8 2.8 5H9.2C9.8 5.8 11.1 4 12 4zM4.3 11h3.6c0 .7 0 1.3.1 2H4.3a8 8 0 010-2zm5.8 2c0-.7-.1-1.3 0-2h3.8v2zm5.9 0c.1-.7.1-1.3 0-2h3.7a8 8 0 010 2zM9.2 15h5.6c-.6 3.2-1.9 5-2.8 5s-2.2-1.8-2.8-5z"/></svg><span>Web: <span class="val">www.kornblatt-betreuung.de</span></span></li>
      <li><svg viewBox="0 0 24 24"><path d="M12 2a7 7 0 00-7 7c0 5 7 13 7 13s7-8 7-13a7 7 0 00-7-7zm0 9.5A2.5 2.5 0 1112 6.5a2.5 2.5 0 010 5z"/></svg><span style="line-height:1.15">Straße &amp; Hausnummer<br>PLZ Ort</span></li>
    </ul>
    <div class="badge" role="img" aria-label="Siegel Betreuungsleistungen"></div>
    <div class="band">Beratungstermin vereinbaren!</div>
  </div>

  <div class="panel front-panel">
    <div class="photo meadow" style="top:300px;bottom:0" role="img" aria-label="Foto zweier Hände, eine ältere und eine jüngere, über einer Blumenwiese"></div>
    <div class="brand">
      <div class="brand-mark"></div>
      <div class="brand-name">Kornblatt</div>
      <div class="brand-line">Ambulanter Betreuungsdienst</div>
      <div class="brand-target">Für Senioren &amp; Menschen mit Beeinträchtigung</div>
    </div>
    <p class="slogan">Verlässlichkeit und Fürsorge<br>mit Herz &amp; Verstand</p>
    <div class="band">Telefon: 0XXX / XXXXXXX</div>
  </div>
</section>

<section class="spread inside">
  <div class="panel inside-left">
    <div class="photo meadow" style="top:260px;bottom:0" role="img" aria-label="Sanfte Blumenwiese als Hintergrund"></div>
    <h2 class="head">Für ein selbstbestimmtes<br>Leben im eigenen Zuhause</h2>
    <p class="intro">Wir unterstützen Senioren und Menschen mit Beeinträchtigungen im Alltag – <b>zuverlässig, respektvoll und individuell</b>. Unser Ziel ist es, Lebensqualität zu erhalten, <b>Angehörige zu entlasten</b> und soziale Teilhabe zu ermöglichen.</p>
    <ul class="features">
      <li><span class="ico blue"></span><span><b>Persönliche &amp; individuelle Betreuung</b></span></li>
      <li><span class="ico blue"></span><span>Anerkannte Leistungen nach <b>SGB XI</b></span></li>
      <li><span class="ico"></span><span><b>Zuverlässige Begleitung</b> im Alltag</span></li>
      <li><span class="ico"></span><span><b>Entlastung</b> für Angehörige</span></li>
      <li><span class="ico blue"></span><span><b>Herzliche &amp; qualifizierte</b> Betreuungskräfte</span></li>
    </ul>
    <h3 class="sec-title" style="top:518px;left:50px">Dienstleistungen im Haushalt</h3>
    <ul class="svc house" style="top:556px;left:60px;width:330px">
      <li><b>Bodenreinigung</b> (Saugen &amp; Wischen)</li>
      <li>Reinigung von <b>Küche &amp; Bad</b></li>
      <li>Betten frisch beziehen</li>
      <li><b>Fensterreinigung</b> (innen &amp; außen)</li>
      <li><b>Haustierbetreuung</b> (z. B. Hund ausführen)</li>
      <li><b>Wäsche</b> waschen</li>
      <li><b>Dekorieren</b></li>
      <li>… und <b>vieles mehr</b></li>
    </ul>
    <div class="illus" style="top:570px;left:400px;width:110px;height:110px" role="img" aria-label="Illustration Reinigungsmittel und Schwamm"></div>
    <div class="band">Beratungstermin vereinbaren!</div>
  </div>

  <div class="panel inside-right">
    <div class="photo meadow" style="top:250px;bottom:0" role="img" aria-label="Sanfte Blumenwiese als Hintergrund"></div>
    <h2 class="head caps">Unsere Leistungen</h2>
    <h3 class="sec-title" style="top:108px;left:150px">Unterstützung im Alltag</h3>
    <ul class="svc" style="top:146px;left:150px;width:390px">
      <li><b>Begleitung</b> zu Arzt-, Therapie- &amp; Behördenterminen</li>
      <li>Hilfe beim <b>Einkaufen &amp; Besorgungen</b> inkl. Transport</li>
      <li>Unterstützung bei <b>Tagesstruktur &amp; Alltagsorganisation</b></li>
      <li><b>Erinnerungsservice</b> (z. B. Medikamenteneinnahme)</li>
      <li>Begleitung zu <b>Freizeit- &amp; Kulturveranstaltungen</b></li>
      <li>Gemeinsames Spazierengehen &amp; <b>Bewegungsangebote</b></li>
      <li><b>Lesen &amp; Vorlesen</b></li>
      <li>Gemeinsames Kochen &amp; <b>Gesellschaft</b> beim Essen</li>
      <li>Unterstützung bei <b>Terminplanung &amp; Kommunikation</b> mit medizinischem Personal</li>
    </ul>
    <div class="illus" style="top:160px;left:25px;width:100px;height:110px" role="img" aria-label="Illustration Begleitung älterer Menschen"></div>
    <h3 class="sec-title" style="top:345px;left:30px">Soziale Betreuung &amp; Aktivierung</h3>
    <ul class="svc" style="top:385px;left:40px;width:310px">
      <li>Gesellschaft leisten &amp; Gespräche führen</li>
      <li>Freizeitaktivitäten planen &amp; durchführen</li>
      <li>Gemeinsames Lesen &amp; Vorlesen</li>
      <li>Karten- &amp; Brettspiele</li>
      <li>Malen, Basteln &amp; kreative Angebote</li>
      <li>Briefe schreiben &amp; E-Mails verfassen</li>
      <li>Alte Interessen wecken &amp; neue entdecken</li>
      <li>Angehörige entlasten</li>
      <li>Regelmäßiger Informationsaustausch mit Angehörigen</li>
    </ul>
    <div class="illus" style="top:400px;left:385px;width:140px;height:110px" role="img" aria-label="Illustration zweier Personen im Gespräch am Tisch"></div>
    <h3 class="sec-title" style="top:565px;left:210px">Betreuung bei Demenz</h3>
    <ul class="svc" style="top:603px;left:220px;width:320px">
      <li>Individuelle Betreuung</li>
      <li>Erinnerungspflege &amp; Biografiearbeit</li>
      <li>Kurz- &amp; Langzeitbetreuung</li>
      <li>Nachtpflege</li>
      <li>Bewegungsangebote</li>
      <li>Spiele &amp; gemeinschaftliche Aktivitäten</li>
    </ul>
    <div class="illus" style="top:580px;left:40px;width:120px;height:120px" role="img" aria-label="Illustration Betreuung bei Demenz"></div>
    <div class="band">Telefon: 0XXX / XXXXXXX</div>
  </div>
</section>

</body>
</html>
```